Quandoria Tours - Astronomy in the Kimberley

Quandoria Tours requires a web page to advertise astronomy tours in the East Kimberley, Australia. It needs the following tabs - Home, Tours, Astronomy Events, Gallery, Testimonials, Contacts.

It should target tourists to the Kimberley.
We are unsure of which colours to go with at the moment but we have included our logo if it helps.

It should be mobile and tablet friendly.

Target Market(s)

Families, +40, Tourist, hobby astronomists,

Industry/Entity Type

Events

Number of Pages Required

3 page

Colors
3377b5
ffffff

Requirements
Must have
• Home, Tours, Astronomy Events, Gallery, Calendar, Testimonials, Contacts.
• 'Quandoria Tours' logo
Nice to have
• Pictures of portable amateur telescopes. Pictures of Lake Kununurra or Wyndham.
Should not have
• Pictures of extremely large professional telescopes.

```html
<!DOCTYPE html>
<html lang="en">
<head>
<meta charset="utf-8">
<title>Quandoria Tours – Astronomy in the Kimberley</title>
<link rel="stylesheet" href="https://fonts.googleapis.com/css2?family=Raleway:wght@300;400;600&family=Open+Sans:wght@400;600;700&display=swap">
<style>
  :root{
    --brand:#3377b5;
    --brand-dark:#1f5f98;
    --white:#ffffff;
    --ink:#333333;
    --muted:#8a8a8a;
    --line:#e6e6e6;
    --space:#04070f;
    --night:#0d1e33;
    --night-2:#1a3552;
    --footer:#000000;
  }
  *{margin:0;padding:0;box-sizing:border-box}
  html,body{width:1200px;height:2714px;overflow:hidden;background:var(--white)}
  body{position:relative;font-family:"Open Sans",Arial,sans-serif;color:var(--ink)}
  .abs{position:absolute}

  /* Hero */
  .hero{position:absolute;left:0;top:0;width:1200px;height:670px;overflow:hidden}
  .hero-sky{position:absolute;inset:0;
    background:
      radial-gradient(ellipse 140px 70px at 1020px 300px,rgba(210,140,90,.55),transparent 70%),
      radial-gradient(ellipse 260px 160px at 1000px 300px,rgba(90,60,120,.35),transparent 75%),
      radial-gradient(circle at 300px 500px,rgba(40,60,110,.25),transparent 40%),
      linear-gradient(180deg,#03050b,#0a0f1c 60%,#05070d)}
  .nav{position:absolute;top:68px;left:0;width:1200px;height:24px;font-family:"Open Sans",sans-serif;font-size:14px;color:var(--white);letter-spacing:.5px}
  .nav a{position:absolute;color:var(--white);text-decoration:none;white-space:nowrap}
  .nav a.active{color:#7fb4e6}
  .nav a.active::after{content:"";position:absolute;left:0;right:0;top:26px;height:2px;background:var(--brand)}
  .brand{position:absolute;left:528px;top:0;width:144px;height:135px;background:rgba(20,30,48,.85);display:flex;flex-direction:column;align-items:center;justify-content:center;gap:8px}
  .brand-dot{width:22px;height:22px;border-radius:50%;background:var(--brand)}
  .brand-name{font-family:"Raleway",sans-serif;font-weight:600;font-size:19px;color:var(--white);text-align:center;line-height:1.1}
  .hero-kicker{position:absolute;left:217px;top:232px;font-family:"Raleway",sans-serif;font-weight:400;font-size:38px;color:var(--white);letter-spacing:1px}
  .hero-rule{position:absolute;left:217px;top:292px;width:150px;height:2px;background:rgba(255,255,255,.7)}
  .hero-title{position:absolute;left:222px;top:318px;width:900px;font-family:"Raleway",sans-serif;font-weight:300;font-size:48px;line-height:58px;color:var(--white)}
  .btn{position:absolute;height:42px;font-family:"Open Sans",sans-serif;font-size:14px;font-weight:600;color:var(--white);display:flex;align-items:center;justify-content:center;letter-spacing:.5px}
  .btn-solid{background:var(--brand)}
  .btn-ghost{border:2px solid rgba(255,255,255,.85)}
  .slide-arrow{position:absolute;top:336px}
  .dot{position:absolute;top:606px;width:20px;height:20px;border:2px solid var(--white)}
  .dot.on{background:var(--white)}

  /* About */
  .about-title{position:absolute;left:136px;top:695px;font-family:"Raleway",sans-serif;font-size:42px;color:var(--ink)}
  .about-rule{position:absolute;left:136px;top:752px;width:190px;height:2px;background:var(--ink)}
  .about-lead{position:absolute;left:136px;top:768px;font-size:15px;color:#555}
  .about-body{position:absolute;left:136px;top:806px;width:300px;font-size:26px;line-height:33px;color:var(--ink)}
  .card{position:absolute;top:814px;width:232px;height:241px;border:1px solid var(--line);padding:22px 24px}
  .card-head{display:flex;align-items:center;gap:10px;font-weight:700;font-size:16px;color:#222;margin-bottom:16px;margin-top:14px}
  .card-text{font-size:12px;line-height:18px;color:var(--muted)}

  /* Gallery */
  .gallery{position:absolute;left:0;top:1085px;width:1200px;height:610px;
    background:
      radial-gradient(circle at 200px 120px,rgba(70,120,170,.35),transparent 40%),
      radial-gradient(circle at 950px 500px,rgba(60,100,150,.3),transparent 45%),
      linear-gradient(180deg,#132a44,#0c1d31 50%,#173250)}
  .gallery-title{position:absolute;left:0;width:1200px;top:40px;text-align:center;font-family:"Raleway",sans-serif;font-size:42px;color:var(--white)}
  .gallery-lead{position:absolute;left:0;width:1200px;top:112px;text-align:center;font-size:15px;color:var(--white)}
  .tile{position:absolute;width:221px;height:166px;display:flex;align-items:center;justify-content:center;font-family:"Raleway",sans-serif;font-size:22px;color:var(--white);box-shadow:0 6px 14px rgba(0,0,0,.45)}
  .tile-a{background:radial-gradient(ellipse 90px 30px at 40% 50%,rgba(170,140,120,.55),transparent 75%),linear-gradient(135deg,#1a2536,#0a0f18)}
  .tile-b{background:radial-gradient(circle at 0% 60%,#8a6040 0,#5a3a26 30%,transparent 55%),linear-gradient(135deg,#0f1a2a,#060a12)}
  .tile-c{background:radial-gradient(circle at 55% 60%,rgba(60,110,170,.5),transparent 55%),linear-gradient(135deg,#0e1d30,#050a12)}
  .tile-d{background:radial-gradient(circle at 100% 55%,#9a7050 0,#5b3e28 32%,transparent 58%),linear-gradient(135deg,#0c1624,#05080f)}

  /* Services */
  .services-title{position:absolute;left:0;width:1200px;top:1747px;text-align:center;font-family:"Raleway",sans-serif;font-size:22px;color:#222;letter-spacing:.5px}
  .service{position:absolute;top:1792px;width:240px;text-align:center}
  .service-name{margin-top:10px;font-size:17px;font-weight:600;color:var(--brand)}
  .service-text{margin-top:8px;font-size:12px;line-height:16px;color:var(--muted)}
  .service-more{margin-top:10px;font-size:12px;font-weight:600;color:var(--brand)}

  /* Video feature */
  .feature{position:absolute;left:0;top:2015px;width:1200px;height:397px;
    background:
      radial-gradient(ellipse 90px 40px at 980px 150px,rgba(220,140,90,.5),transparent 70%),
      radial-gradient(ellipse 160px 220px at 0px 200px,rgba(140,150,180,.35),transparent 70%),
      linear-gradient(180deg,#05070d,#0a0e18 55%,#04060b)}
  .video{position:absolute;left:84px;top:53px;width:435px;height:278px;background:radial-gradient(circle at 55% 40%,#dfe6ee 0,#9fb6cc 25%,#3a6a96 55%,#16324f 100%)}
  .video-bar{position:absolute;left:0;bottom:0;width:435px;height:30px;background:rgba(0,0,0,.8);display:flex;align-items:center;gap:10px;padding:0 10px;font-size:10px;color:#ccc}
  .video-track{flex:1;height:4px;background:#555;position:relative}
  .video-track i{position:absolute;left:0;top:0;height:4px;width:55%;background:var(--brand)}
  .feature-title{position:absolute;left:558px;top:58px;font-family:"Raleway",sans-serif;font-weight:600;font-size:22px;color:var(--white)}
  .feature-text{position:absolute;left:558px;top:92px;width:580px;font-size:14px;line-height:19px;color:var(--white)}
  .checks{position:absolute;left:575px;top:142px;list-style:none}
  .checks li{display:flex;align-items:center;gap:14px;height:39px;font-size:15px;color:var(--white)}

  /* Footer */
  .footer{position:absolute;left:0;top:2412px;width:1200px;height:302px;background:var(--footer)}
  .footer-brand{position:absolute;left:0;width:1200px;top:44px;display:flex;flex-direction:column;align-items:center;gap:8px}
  .footer-links{position:absolute;left:0;width:1200px;top:174px;text-align:center;font-size:12px;color:var(--white)}
  .footer-links span{margin:0 5px}
  .socials{position:absolute;left:0;width:1200px;top:206px;display:flex;justify-content:center;gap:12px}
  .socials i{width:22px;height:22px;border-radius:50%;background:var(--white);display:block}
  .copyright{position:absolute;left:0;width:1200px;top:240px;text-align:center;font-size:11px;color:#bbb}
</style>
</head>
<body>

<header class="hero">
  <div class="hero-sky" role="img" aria-label="Night sky full of stars with a glowing spiral galaxy on the right"></div>
  <nav class="nav">
    <a class="active" style="left:140px">HOME</a>
    <a style="left:232px">TOURS &#9662;</a>
    <a style="left:318px">ASTRONOMY EVENTS</a>
    <a style="left:772px">GALLERY</a>
    <a style="left:872px">TESTIMONIALS</a>
    <a style="left:1008px">CONTACTS</a>
  </nav>
  <div class="brand">
    <span class="brand-dot"></span>
    <span class="brand-name">Quandoria<br>Tours</span>
  </div>
  <div class="hero-kicker">QUANDORIA</div>
  <div class="hero-rule"></div>
  <h1 class="hero-title">Lorem Ipsum is simply dummy text of the printing and</h1>
  <a class="btn btn-solid" style="left:232px;top:480px;width:128px">LOGIN</a>
  <a class="btn btn-ghost" style="left:374px;top:480px;width:128px">LEARN MORE</a>
  <svg class="slide-arrow" style="left:82px" width="20" height="34" viewBox="0 0 20 34"><path d="M17 2 3 17l14 15" fill="none" stroke="#fff" stroke-opacity=".6" stroke-width="3"/></svg>
  <svg class="slide-arrow" style="left:1096px" width="20" height="34" viewBox="0 0 20 34"><path d="M3 2l14 15L3 32" fill="none" stroke="#fff" stroke-opacity=".6" stroke-width="3"/></svg>
  <span class="dot on" style="left:683px"></span>
  <span class="dot" style="left:718px"></span>
  <span class="dot" style="left:753px"></span>
</header>

<section class="about">
  <h2 class="about-title">About Us</h2>
  <div class="about-rule"></div>
  <p class="about-lead">Lorem Ipsum is simply dummy text of the printing and</p>
  <p class="about-body">Lorem Ipsum is simply dummy text of the printing and typesetting s industry. Lorem Ipsum</p>
  <a class="btn btn-solid" style="left:136px;top:1008px;width:205px;height:44px;font-weight:400;font-size:14px">For More Info Click Here</a>

  <div class="card" style="left:537px">
    <div class="card-head">
      <svg width="30" height="24" viewBox="0 0 30 24"><g fill="none" stroke="#555" stroke-width="1.6"><circle cx="5" cy="18" r="3"/><circle cx="15" cy="6" r="3"/><circle cx="26" cy="14" r="3"/><path d="M7 16l6-8M18 7l6 5"/></g></svg>
      LOREM IPSUM
    </div>
    <p class="card-text">Lorem Ipsum is simply dummy text of the printing and typesetting industry. Lorem Ipsum has been the industry's standard dummy text ever since the 1500s, when</p>
  </div>
  <div class="card" style="left:820px">
    <div class="card-head">
      <svg width="30" height="24" viewBox="0 0 30 24"><g fill="none" stroke="#555" stroke-width="1.6"><circle cx="6" cy="5" r="3"/><path d="M8 7l14 14M22 21l4-2"/></g></svg>
      LOREM IPSUM
    </div>
    <p class="card-text">Lorem Ipsum is simply dummy text of the printing and typesetting industry. Lorem Ipsum has been the industry's standard dummy text ever since the 1500s, when</p>
  </div>
</section>

<section class="gallery" role="img" aria-label="Deep blue starry night sky backdrop">
  <h2 class="gallery-title">Quandoria</h2>
  <p class="gallery-lead">Lorem Ipsum is simply dummy text of the printing and typesetting industry.</p>
  <div class="tile tile-a" role="img" aria-label="Spiral galaxy in deep space" style="left:90px;top:166px">Lorem Ipsum</div>
  <div class="tile tile-b" role="img" aria-label="Edge of a large planet against stars" style="left:356px;top:166px">Lorem Ipsum</div>
  <div class="tile tile-c" role="img" aria-label="Blue nebula among stars" style="left:621px;top:166px">Lorem Ipsum</div>
  <div class="tile tile-d" role="img" aria-label="Planet rising at the edge of space" style="left:883px;top:166px">Lorem Ipsum</div>
  <div class="tile tile-a" role="img" aria-label="Spiral galaxy in deep space" style="left:90px;top:368px">Lorem Ipsum</div>
  <div class="tile tile-b" role="img" aria-label="Edge of a large planet against stars" style="left:356px;top:368px">Lorem Ipsum</div>
  <div class="tile tile-c" role="img" aria-label="Blue nebula among stars" style="left:621px;top:368px">Lorem Ipsum</div>
  <div class="tile tile-d" role="img" aria-label="Planet rising at the edge of space" style="left:883px;top:368px">Lorem Ipsum</div>
</section>

<section class="services">
  <h2 class="services-title">OUR SERVICES</h2>
  <div class="service" style="left:70px">
    <svg width="36" height="36" viewBox="0 0 36 36"><g fill="none" stroke="#3377b5" stroke-width="3"><rect x="4" y="6" width="24" height="24"/><path d="M10 17l6 6L32 5"/></g></svg>
    <div class="service-name">Lorem Ipsum</div>
    <p class="service-text">Lorem Ipsum is simply dummy text of the printing and typesetting industry. Lorem Ipsum has been the</p>
    <div class="service-more">Read More</div>
  </div>
  <div class="service" style="left:341px">
    <svg width="36" height="36" viewBox="0 0 36 36"><g fill="none" stroke="#3377b5" stroke-width="2.4"><circle cx="18" cy="18" r="14"/><ellipse cx="18" cy="18" rx="6" ry="14"/><path d="M4 18h28M7 10h22M7 26h22"/></g></svg>
    <div class="service-name">Lorem Ipsum</div>
    <p class="service-text">Lorem Ipsum is simply dummy text of the printing and typesetting industry. Lorem Ipsum has been the</p>
    <div class="service-more">Read More</div>
  </div>
  <div class="service" style="left:613px">
    <svg width="36" height="36" viewBox="0 0 36 36"><g fill="none" stroke="#3377b5" stroke-width="2.4"><circle cx="18" cy="18" r="10"/><ellipse cx="18" cy="18" rx="17" ry="6" transform="rotate(-25 18 18)"/></g></svg>
    <div class="service-name">Lorem Ipsum</div>
    <p class="service-text">Lorem Ipsum is simply dummy text of the printing and typesetting industry. Lorem Ipsum has been the</p>
    <div class="service-more">Read More</div>
  </div>
  <div class="service" style="left:890px">
    <svg width="36" height="36" viewBox="0 0 36 36"><g fill="#3377b5"><circle cx="18" cy="5" r="4"/><path d="M12 11h12v13h-3v11h-6V24h-3z"/></g></svg>
    <div class="service-name">Lorem Ipsum</div>
    <p class="service-text">Lorem Ipsum is simply dummy text of the printing and typesetting industry. Lorem Ipsum has been the</p>
    <div class="service-more">Read More</div>
  </div>
</section>

<section class="feature" role="img" aria-label="Starry night sky with a distant galaxy">
  <div class="video" role="img" aria-label="Video still of an astronaut floating above the Earth">
    <div class="video-bar">
      <svg width="10" height="12" viewBox="0 0 10 12"><path d="M0 0l10 6-10 6z" fill="#ccc"/></svg>
      <span>00:12</span>
      <span class="video-track"><i></i></span>
      <span>04:32</span>
      <svg width="14" height="12" viewBox="0 0 14 12"><path d="M0 4h3l4-4v12L3 8H0z" fill="#ccc"/></svg>
      <svg width="14" height="12" viewBox="0 0 14 12"><rect x="1" y="1" width="12" height="10" fill="none" stroke="#ccc" stroke-width="1.5"/></svg>
    </div>
  </div>
  <h3 class="feature-title">Lorem Ipsum is simply dummy text</h3>
  <p class="feature-text">Lorem Ipsum is simply dummy text of the printing and typesetting industry. Lorem Ipsum has been the industry's standard dummy text ever since the 1500s</p>
  <ul class="checks">
    <li><svg width="22" height="22" viewBox="0 0 22 22"><circle cx="11" cy="11" r="11" fill="#3377b5"/><path d="M6 11l4 4 6-7" fill="none" stroke="#fff" stroke-width="2.2"/></svg>Lorem Ipsum is simply dummy</li>
    <li><svg width="22" height="22" viewBox="0 0 22 22"><circle cx="11" cy="11" r="11" fill="#3377b5"/><path d="M6 11l4 4 6-7" fill="none" stroke="#fff" stroke-width="2.2"/></svg>Many desktop publishing packages and web</li>
    <li><svg width="22" height="22" viewBox="0 0 22 22"><circle cx="11" cy="11" r="11" fill="#3377b5"/><path d="M6 11l4 4 6-7" fill="none" stroke="#fff" stroke-width="2.2"/></svg>All the Lorem Ipsum generators on</li>
    <li><svg width="22" height="22" viewBox="0 0 22 22"><circle cx="11" cy="11" r="11" fill="#3377b5"/><path d="M6 11l4 4 6-7" fill="none" stroke="#fff" stroke-width="2.2"/></svg>The standard chunk of</li>
    <li><svg width="22" height="22" viewBox="0 0 22 22"><circle cx="11" cy="11" r="11" fill="#3377b5"/><path d="M6 11l4 4 6-7" fill="none" stroke="#fff" stroke-width="2.2"/></svg>It was popularised in the 1960s with</li>
  </ul>
</section>

<footer class="footer">
  <div class="footer-brand">
    <span class="brand-dot"></span>
    <span class="brand-name">Quandoria Tours</span>
  </div>
  <p class="footer-links"><span>Home</span>|<span>About Us</span>|<span>Tour</span>|<span>Privacy policy</span>|<span>Term &amp; Condition</span></p>
  <div class="socials"><i></i><i></i><i></i></div>
  <p class="copyright">Copyright ©2015. Quandoria Tours, All Rights Reserved</p>
</footer>

</body>
</html>
```